8"x5" postcard for Wireless Internet introduction to new mountain town market

I need to market high speed internet to a resort mountain town without doing the obvious laptop on a mountain top thing, so tired. We are going to be competing directly with another provider with same cost, but we will be offering free installation. The area is Aspen Colorado, so the clientele are outdoor types who have suffered for years from being disconnected in their mountain town. We offer fast internet and excellent customer service from people who live in their neck of the woods.

Target Market(s)

23-55 years old, both resort living, families and ski bums

Font styles to use
Sans Serif

Colors

Designer to choose colors to be used in the design.

Requirements
Must have
• Visual appeal and fresh verbiage. We don't mind being a little edgy. We are a young company and we want to appeal to people looking for a provider who gets them. We prefer a clean look.
Nice to have
• Nice to have colors that match our logo
Should not have
• stuffy concepts or verbiage that is too much like a car salesman. We don't want to look like a 'big box' company.

```html
<!DOCTYPE html>
<html lang="en">
<head>
<meta charset="utf-8">
<title>Super Fast Wireless Internet – Summit Wave Postcard</title>
<link rel="stylesheet" href="https://fonts.googleapis.com/css2?family=Exo+2:ital,wght@1,900&family=Montserrat:wght@400;600;700;800;900&display=swap">
<style>
  :root {
    --backdrop: #6a6a6a;
    --paper: #ffffff;
    --panel: #f3f4f6;
    --ink: #0b0b0b;
    --slate: #4a4a4c;
    --yellow: #f7e01d;
    --amber: #f9b43c;
    --orange: #f39a2b;
    --sky-top: #dfe9f3;
    --sky-low: #c6d6e2;
    --grass: #4f8a34;
    --grass-deep: #3f7427;
    --ghost: rgba(110, 110, 110, 0.28);
  }
  html, body {
    margin: 0;
    padding: 0;
    width: 1093px;
    height: 1200px;
    overflow: hidden;
    background: var(--backdrop);
  }
  .postcard {
    position: absolute;
    left: 196px;
    top: 40px;
    width: 700px;
    height: 1120px;
    display: block;
    background: var(--paper);
  }
  .headline {
    font-family: "Exo 2", "Montserrat", sans-serif;
    font-style: italic;
    font-weight: 900;
  }
  .headline-fill { fill: var(--yellow); }
  .headline-edge { fill: var(--orange); }
  .headline-ghost { fill: var(--ghost); }
  .subhead {
    font-family: "Montserrat", sans-serif;
    font-weight: 400;
    font-size: 30px;
    letter-spacing: 1px;
    fill: var(--ink);
  }
  .badge-text,
  .feature,
  .price-tag,
  .cta-title,
  .cta-phone {
    font-family: "Montserrat", sans-serif;
    font-weight: 800;
    fill: var(--ink);
  }
  .badge-text { font-size: 30px; }
  .feature { font-size: 38px; }
  .price-tag { font-size: 23px; }
  .speed {
    font-family: "Montserrat", sans-serif;
    font-weight: 900;
    font-size: 118px;
    letter-spacing: -6px;
    fill: var(--ink);
  }
  .speed-unit {
    font-family: "Montserrat", sans-serif;
    font-weight: 600;
    font-size: 23px;
    fill: var(--ink);
  }
  .cta-title { font-size: 42px; font-weight: 900; }
  .cta-phone { font-size: 33px; }
  .brand-name {
    font-family: "Montserrat", sans-serif;
    font-weight: 700;
    font-size: 34px;
    fill: var(--slate);
  }
  .web-line {
    font-family: "Montserrat", sans-serif;
    font-weight: 400;
    font-size: 22px;
    fill: var(--ink);
  }
  .web-line .web-address { font-weight: 800; }
</style>
</head>
<body>
<svg class="postcard" viewBox="0 0 825 1320" xmlns="http://www.w3.org/2000/svg">
  <defs>
    <linearGradient id="sceneTone" x1="0" y1="0" x2="0" y2="1">
      <stop offset="0" stop-color="var(--sky-top)"/>
      <stop offset="0.4" stop-color="var(--sky-low)"/>
      <stop offset="0.5" stop-color="#7ea35c"/>
      <stop offset="0.62" stop-color="var(--grass)"/>
      <stop offset="1" stop-color="var(--grass-deep)"/>
    </linearGradient>
    <linearGradient id="sunBadge" x1="0" y1="0" x2="1" y2="0">
      <stop offset="0" stop-color="var(--yellow)"/>
      <stop offset="1" stop-color="var(--amber)"/>
    </linearGradient>
    <linearGradient id="ctaBand" x1="0" y1="0" x2="1" y2="0">
      <stop offset="0" stop-color="var(--amber)"/>
      <stop offset="1" stop-color="var(--yellow)"/>
    </linearGradient>
  </defs>

  <!-- hero scene -->
  <rect class="hero-scene" x="0" y="0" width="825" height="720" fill="url(#sceneTone)" role="img" aria-label="Photo of a cheetah sprinting across a blurred green meadow under a cloudy sky"/>

  <!-- headline with motion echoes -->
  <g class="headline">
    <text class="headline-ghost" x="115" y="108" font-size="74" textLength="355" lengthAdjust="spacingAndGlyphs">SUPER</text>
    <text class="headline-ghost" x="255" y="108" font-size="74" textLength="355" lengthAdjust="spacingAndGlyphs">SUPER</text>
    <text class="headline-edge" x="170" y="111" font-size="74" textLength="355" lengthAdjust="spacingAndGlyphs">SUPER</text>
    <text class="headline-fill" x="165" y="107" font-size="74" textLength="355" lengthAdjust="spacingAndGlyphs">SUPER</text>

    <text class="headline-ghost" x="240" y="198" font-size="94" textLength="335" lengthAdjust="spacingAndGlyphs">FAST</text>
    <text class="headline-ghost" x="370" y="198" font-size="94" textLength="335" lengthAdjust="spacingAndGlyphs">FAST</text>
    <text class="headline-edge" x="291" y="201" font-size="94" textLength="335" lengthAdjust="spacingAndGlyphs">FAST</text>
    <text class="headline-fill" x="286" y="197" font-size="94" textLength="335" lengthAdjust="spacingAndGlyphs">FAST</text>
  </g>
  <text class="subhead" x="395" y="250" text-anchor="middle">WIRELESS INTERNET</text>

  <!-- speed stripes -->
  <g class="speed-stripes">
    <polygon points="0,453 240,560 0,505" fill="var(--ink)"/>
    <polygon points="0,505 240,560 0,578" fill="var(--slate)"/>
    <polygon points="0,573 825,518 825,524 0,613" fill="var(--yellow)"/>
    <polygon points="0,613 825,524 825,530 0,648" fill="var(--amber)"/>
    <polygon points="0,648 825,530 825,548 0,710" fill="var(--ink)"/>
    <polygon points="0,710 825,548 825,1320 0,1320" fill="var(--paper)"/>
  </g>

  <!-- slogan badge -->
  <g class="slogan-badge">
    <circle cx="413" cy="575" r="128" fill="var(--paper)"/>
    <circle cx="413" cy="575" r="118" fill="url(#sunBadge)"/>
    <text class="badge-text" x="413" y="543" text-anchor="middle">BETTER,</text>
    <text class="badge-text" x="413" y="584" text-anchor="middle">NOT</text>
    <text class="badge-text" x="413" y="626" text-anchor="middle">BIGGER!</text>
  </g>

  <!-- perks -->
  <g class="perks">
    <text class="feature" x="93" y="751">FREE</text>
    <text class="feature" x="93" y="788">RESIDENTIAL</text>
    <text class="feature" x="93" y="825">INSTALLATION</text>

    <line x1="452" y1="728" x2="452" y2="826" stroke="var(--ink)" stroke-width="3"/>
    <circle cx="452" cy="777" r="22" fill="var(--ink)"/>
    <polyline points="446,767 457,777 446,787" fill="none" stroke="var(--paper)" stroke-width="4" stroke-linecap="round" stroke-linejoin="round"/>

    <text class="feature" x="518" y="751">IN-HOUSE</text>
    <text class="feature" x="518" y="788">TECH</text>
    <text class="feature" x="518" y="825">SUPPORT</text>
  </g>

  <!-- speed tiers -->
  <rect class="speed-panel" x="0" y="905" width="825" height="181" fill="var(--panel)"/>
  <polygon class="price-ribbon" points="0,863 400,863 418,889 400,915 0,915" fill="url(#sunBadge)"/>
  <text class="price-tag" x="44" y="898">PRICES START AT $59.95</text>

  <g class="speed-tiers">
    <text class="speed" x="82" y="1036">10</text>
    <text class="speed-unit" x="98" y="1058">mbps</text>

    <line x1="277" y1="960" x2="277" y2="1040" stroke="var(--ink)" stroke-width="2"/>
    <circle cx="277" cy="1001" r="10" fill="var(--ink)"/>
    <polyline points="274,996 279,1001 274,1006" fill="none" stroke="var(--paper)" stroke-width="2.5" stroke-linecap="round"/>

    <text class="speed" x="332" y="1036">25</text>
    <text class="speed-unit" x="336" y="1058">mbps</text>

    <line x1="525" y1="960" x2="525" y2="1040" stroke="var(--ink)" stroke-width="2"/>
    <circle cx="525" cy="1001" r="10" fill="var(--ink)"/>
    <polyline points="522,996 527,1001 522,1006" fill="none" stroke="var(--paper)" stroke-width="2.5" stroke-linecap="round"/>

    <text class="speed" x="574" y="1036">40</text>
    <text class="speed-unit" x="578" y="1058">mbps</text>
  </g>

  <!-- brand and call to action -->
  <rect class="brand-band" x="0" y="1113" width="825" height="127" fill="var(--panel)"/>
  <g class="brand">
    <circle cx="76" cy="1173" r="28" fill="var(--amber)"/>
    <text class="brand-name" x="118" y="1186">Summit Wave</text>
  </g>
  <polygon class="cta-band" points="452,1088 825,1088 825,1240 452,1240 390,1164" fill="url(#ctaBand)"/>
  <text class="cta-title" x="772" y="1151" text-anchor="end">CALL NOW!</text>
  <text class="cta-phone" x="772" y="1199" text-anchor="end">1 888 555 0147</text>

  <text class="web-line" x="413" y="1291" text-anchor="middle">VISIT US ONLINE AT <tspan class="web-address">WWW.SUMMITWAVE.NET/PEAK</tspan></text>
</svg>
</body>
</html>
```